Sterling Floorworks Letterhead

Letterhead used for business reasons. It must be editable and easy to use.

Address is 5127 W. Harbor Lane Brookhaven FL 33871 - 555.382.5519

```html
<!DOCTYPE html>
<html lang="en">
<head>
<meta charset="utf-8">
<title>Sterling Floorworks Letterhead</title>
<link href="https://fonts.googleapis.com/css2?family=Open+Sans:wght@300;400&family=Great+Vibes&display=swap" rel="stylesheet">
<style>
  :root {
    --backdrop: #e6e6e6;
    --paper: #f2f2f2;
    --ink: #333333;
    --brand-orange: #d4831f;
    --footer-dark: #3a3a3c;
    --footer-text: #ffffff;
  }
  * { margin: 0; padding: 0; box-sizing: border-box; }
  html, body {
    width: 1200px; height: 1200px; overflow: hidden;
    background: var(--backdrop);
    font-family: "Open Sans", Arial, sans-serif;
  }
  .letterhead {
    position: absolute; left: 196px; top: 30px;
    width: 808px; height: 1140px;
    background: var(--paper);
    box-shadow: 0 4px 18px rgba(0,0,0,0.18);
    overflow: hidden;
  }
  .brand-name {
    position: absolute; top: 50px; left: 0; width: 100%;
    text-align: center;
    font-weight: 400; font-size: 30px; letter-spacing: 0.5px;
    color: var(--brand-orange);
  }
  .letter-body {
    position: absolute; left: 109px; top: 268px; width: 590px;
    color: var(--ink); font-weight: 300; font-size: 13.2px; line-height: 19px;
  }
  .salutation { margin-bottom: 18px; }
  .letter-body p.paragraph { text-align: justify; margin-bottom: 19px; }
  .closing { margin-top: 52px; }
  .signature {
    font-family: "Great Vibes", cursive;
    font-size: 28px; color: #222; margin: 4px 0 0 6px; line-height: 34px;
  }
  .footer-rule {
    position: absolute; left: 0; top: 1032px; width: 808px; height: 4px;
    background: var(--brand-orange);
  }
  .footer-band {
    position: absolute; left: 0; top: 1040px; width: 808px; height: 100px;
    background: var(--footer-dark);
  }
  .contact {
    position: absolute; left: 78px; top: 1074px;
    font-style: normal;
    color: var(--footer-text); font-size: 13px; line-height: 18px; font-weight: 400;
  }
  .contact span { display: block; }
  .contact .phone { display: flex; align-items: center; gap: 6px; }
  .website {
    position: absolute; right: 62px; top: 1092px;
    color: var(--footer-text); font-size: 13px; line-height: 18px; font-weight: 400;
  }
</style>
</head>
<body>
  <main class="letterhead">
    <header class="brand-name">Sterling Floorworks</header>

    <section class="letter-body">
      <p class="salutation">Dear Daniel Hargrove,</p>
      <p class="paragraph">Lorem ipsum dolor sit amet, consectetuer adipiscing elit, sed diam nonummy nibh euismod tincidunt ut laoreet dolore magna aliquam erat volutpat. Ut wisi enim ad minim veniam, quis nostrud exerci tation ullamcorper suscipit lobortis nisl ut aliquip ex ea commodo consequat. Duis dolore te feugait nulla facilisi. Nam liber tempor cum soluta nobis eleifend option congue nihil imperdiet doming id quod mazim placerat facer possim assum. Lorem ipsum dolor sit amet, consectetuer adipiscing elit, sed diam nonummy nibh euismod tincidunt ut laoreet dolore magna aliquam erat volutpat. Ut wisi enim ad minim veniam, quis nostrud exerci tation ullamcorper suscipit lobortis nisl ut aliquip ex ea commodo consequat.</p>
      <p class="paragraph">Consectetuer adipiscing elit, sed diam nonummy nibh euismod tincidunt ut laoreet dolore magna aliquam erat volutpat. Ut wisi enim ad minim veniam, quis nostrud exerci tation ullamcorper suscipit lobortis nisl ut aliquip ex ea commodo consequat. Consectetuer adipiscing elit, sed diam nonummy nibh euismod tincidunt ut laoreet dolore magna aliquam erat volutpat. Ut wisi enim ad minim veniam, quis nostrud exerci tation ullamcorper suscipit lobortis nisl ut aliquip ex ea commodo consequat.</p>
      <p class="paragraph">Consectetuer adipiscing elit, sed diam nonummy nibh euismod tincidunt ut laoreet dolore magna aliquam erat volutpat. Ut wisi enim ad minim veniam, quis nostrud exerci tation ullamcorper suscipit lobortis nisl ut aliquip ex ea commodo consequat. Consectetuer adipiscing elit, sed diam nonummy nibh euismod tincidunt ut laoreet dolore magna aliquam erat volutpat. Ut wisi enim ad minim veniam, quis nostrud exerci tation ullamcorper suscipit lobortis nisl ut aliquip ex ea commodo consequat.</p>
      <p class="closing">Sincerely Yours</p>
      <p class="signature">Thomas Whitfield</p>
    </section>

    <div class="footer-rule" aria-hidden="true"></div>
    <div class="footer-band" aria-hidden="true"></div>

    <address class="contact">
      <span class="phone">
        <svg width="11" height="11" viewBox="0 0 24 24" aria-hidden="true"><path fill="var(--brand-orange)" d="M6.6 10.8a15.1 15.1 0 0 0 6.6 6.6l2.2-2.2c.3-.3.7-.4 1-.2 1.1.4 2.3.6 3.6.6.6 0 1 .4 1 1V20c0 .6-.4 1-1 1A17 17 0 0 1 3 4c0-.6.4-1 1-1h3.5c.6 0 1 .4 1 1 0 1.3.2 2.5.6 3.6.1.3 0 .7-.2 1z"/></svg>
        555.382.5519
      </span>
      <span>5127 W. Harbor Lane Brookhaven FL 33871</span>
    </address>
    <div class="website">www.sterlingfloorworks.com</div>
  </main>
</body>
</html>
```